Buchcover-Design für Detoxkur
Vielen lieben Dank für die professionelle Zusammenarbeit, die sich auch im zweiten Projekt erfolgreich bestätigen ließ. Tip Top! Dankeschön!!!!
Zielgruppe
Ich bin Gesundheits- und Ernährungsberater und suche nach einem Buchcover für mein neues Projekt (Taschenbuch und E-Book) Meine Zielgruppe sind Menschen die auf der Suche nach Heilung und mehr Wohlbefinden sind. (Detoxkur-Entschlacken und Entgiften etc....)
Aufgabenstellung
Das Design sollte durch den Titel deutlich auffallen. Vorzugsweise ein dunkler Hintergrund, Titel in großer Schrift. Eingearbeitet etwas Gemüse und Obst, grüner Saft oder auch ein Smoothie, Zitronenwasser, Magen- und Darmtrakt oder ähnlichem. Es darf auch verspielt sein aber dennoch Niveauvoll.
Das Buch einschließlich Titel und Untertitel, sowie Klappentext werden derzeit von einem Lektor bearbeitet, also können diesbezüglich noch leichte Änderungen anfallen die dann anzupassen wären.
Das Buchformat ist 12cm x 19cm. Die Endgültigen Abmaße müssten nach dem Buchindesign noch angepasst werden, wenn die Seitenzahlen feststehen.
Würde gerne den Coverdesigner im Impressum des Buchs erwähnen und Bitte darum um Einverständnis, wenn es auch erwünscht sein sollte!
Derzeitiger Text :
Titel: Morgenlicht - Finde Ruhe durch Wandern und Tagträumen
Untertitel: - Durch Entgiften und Entschlacken das Wohlbefinden steigern, die Darmgesundheit wieder herstellen, das Gewicht reduzieren und die Heilung für Körper und Geist einleiten -
Klappentext: Bist du auf der Suche nach mehr Wohlbefinden und möchtest deine Gesundheit nachhaltig verbessern? Suchst du nach Methoden deinen Körper von Schadstoffen zu befreien, die dich in der Vergangenheit belastet haben? Möglicherweise fragst du dich warum das so ist und was es damit auf sich hat?
Detox, Entschlacken und Entgiften, Diäten und eine gesündere Ernährungsweise ist in aller Munde. Der Grund dafür ist bei zahlreichen Menschen ein mangelndes Wohlbefinden durch zivillisationsbedingte Einflüsse wie Umweltverschmutzungen, Stress und eine unbewusste Ernährungsweise. Diese Faktoren führen zu krankhaften Symptomen, Energie- und Antriebslosigkeit und letztendlich zu den steigenden Zahlen übergewichtiger Menschen in unserer Bevölkerung.
In diesem Ratgeber erfährst du, wie wichtig es ist sich zu entgiften und wie wichtig dafür eine gesunde Ernähru..

```html
<!DOCTYPE html>
<html lang="de">
<head>
<meta charset="utf-8">
<title>Morgenlicht – Buchumschlag</title>
<link rel="stylesheet" href="https://fonts.googleapis.com/css2?family=Raleway:wght@300;400&family=Open+Sans:wght@400&display=swap">
<style>
  :root {
    --page: #ffffff;
    --cover: #1f1f1f;
    --edge: #5a5a5a;
    --title: #ffffff;
    --accent: #7cc142;
    --muted: #3a3a3a;
    --rule: #bdbdbd;
  }
  * { margin: 0; padding: 0; box-sizing: border-box; }
  html, body { width: 1200px; height: 938px; overflow: hidden; background: var(--page); }
  .jacket {
    position: absolute; left: 28px; top: 28px; width: 1144px; height: 880px;
    background: var(--cover); overflow: hidden;
  }
  .spine-edge { position: absolute; top: 0; bottom: 0; width: 1px; background: var(--edge); }
  .spine-edge.left { left: 535px; }
  .spine-edge.right { left: 617px; }

  .fruit-slice {
    position: absolute; border-radius: 50%;
    background: radial-gradient(circle, #2c2c2c 0%, #262626 60%, #1f1f1f 100%);
  }
  .fruit-slice.back { left: 385px; top: -70px; width: 170px; height: 170px; }
  .fruit-slice.front { left: 990px; top: -70px; width: 170px; height: 170px; }

  /* Rückseite */
  .back-title {
    position: absolute; left: 70px; top: 152px; width: 420px;
    font: 300 46px/1 "Raleway", sans-serif; letter-spacing: 6px; color: var(--title);
  }
  .blurb {
    position: absolute; left: 70px; top: 248px; width: 420px;
    font: 400 13.6px/20.4px "Open Sans", sans-serif; color: var(--accent);
    text-align: justify; hyphens: auto;
  }
  .blurb p + p { margin-top: 20px; }
  .price {
    position: absolute; left: 350px; top: 838px;
    font: 400 12px/1 "Open Sans", sans-serif; color: var(--muted);
  }

  /* Buchrücken */
  .spine-text {
    position: absolute; left: 576px; top: 0; height: 880px;
    writing-mode: vertical-rl; white-space: nowrap;
    font-family: "Raleway", sans-serif; font-size: 15.5px; letter-spacing: 1px;
    transform: translateX(-50%);
  }
  .spine-author { position: absolute; top: 150px; color: var(--title); font-weight: 300; }
  .spine-title { position: absolute; top: 330px; color: var(--accent); font-weight: 400; }

  /* Vorderseite */
  .front { position: absolute; left: 618px; top: 0; width: 526px; height: 880px; }
  .author {
    position: absolute; left: 0; right: 0; top: 52px; text-align: center;
    font: 300 16px/1 "Raleway", sans-serif; letter-spacing: 1.5px; color: #d8d8d8;
  }
  .author-rule { position: absolute; left: 203px; width: 120px; top: 80px; height: 1px; background: var(--rule); }
  .front-title {
    position: absolute; left: 0; right: 0; top: 152px; text-align: center;
    font: 300 54px/1 "Raleway", sans-serif; letter-spacing: 6px; color: var(--title);
  }
  .front-subtitle {
    position: absolute; left: 0; right: 0; top: 247px; text-align: center;
    font: 400 15px/1 "Raleway", sans-serif; letter-spacing: 0.3px; color: var(--accent);
  }
  .hero {
    position: absolute; left: 40px; top: 290px; width: 440px; height: 440px;
  }
  .closing-rule { position: absolute; left: 183px; width: 160px; top: 764px; height: 1px; background: var(--rule); }
  .claim {
    position: absolute; left: 50px; right: 50px; top: 789px; text-align: center;
    font: 400 13.4px/20px "Open Sans", sans-serif; color: #e6e6e6;
  }
</style>
</head>
<body>
<div class="jacket">
  <div class="spine-edge left"></div>
  <div class="spine-edge right"></div>

  <div class="fruit-slice back" role="img" aria-label="Zitronenscheibe als feine Linienzeichnung"></div>
  <div class="fruit-slice front" role="img" aria-label="Zitronenscheibe als feine Linienzeichnung"></div>

  <section class="back-cover">
    <h2 class="back-title">MORGENLICHT</h2>
    <div class="blurb">
      <p>Bist du auf der Suche nach mehr Wohlbefinden und möchtest deine Gesundheit nachhaltig verbessern? Suchst du nach Methoden deinen Körper von Schadstoffen zu befreien, die dich in der Vergangenheit belastet haben? Möglicherweise fragst du dich warum das so ist und was es damit auf sich hat?</p>
      <p>Detox, Entschlacken und Entgiften, Diäten und eine gesündere Ernährungsweise ist in aller Munde. Der Grund dafür ist bei zahlreichen Menschen ein mangelndes Wohlbefinden durch zivillisationsbedingte Einflüsse wie Umweltverschmutzungen, Stress und eine unbewusste Ernährungsweise. Diese Faktoren führen zu krankhaften Symptomen, Energie- und Antriebslosigkeit und letztendlich zu den steigenden Zahlen übergewichtiger Menschen in unserer Bevölkerung.</p>
      <p>In diesem Ratgeber erfährst du, wie wichtig es ist sich zu entgiften und wie wichtig dafür eine gesunde Ernährungsweise ist. Zusätzlich erfährst du, wie du praktische Heilmethoden anwendest, die die Darmgesundheit wiederherstellen und wie du die Entgiftung in den einzelnen Bereichen des Körpers vorantreibst. Denn Detox ist heutzutage wichtiger denn je!</p>
    </div>
    <div class="price">14,95 €</div>
  </section>

  <div class="spine-text">
    <span class="spine-author">LUKAS BRENNER</span>
    <span class="spine-title">MORGENLICHT - FINDE RUHE DURCH WANDERN &amp; TAGTRÄUMEN</span>
  </div>

  <section class="front">
    <div class="author">LUKAS BRENNER</div>
    <div class="author-rule"></div>
    <h1 class="front-title">MORGENLICHT</h1>
    <div class="front-subtitle">FINDE RUHE DURCH WANDERN &amp; TAGTRÄUMEN</div>
    <svg class="hero" viewBox="0 0 440 440" role="img" aria-label="Foto: Zitronenscheibe fällt spritzend in ein Wasserglas, umgeben von gezeichneten Zitronen und Kräutern">
      <defs>
        <radialGradient id="heroGlow" cx="50%" cy="58%" r="50%">
          <stop offset="0%" stop-color="#6b6a52"/>
          <stop offset="35%" stop-color="#3d3d36"/>
          <stop offset="75%" stop-color="#262626"/>
          <stop offset="100%" stop-color="#1f1f1f"/>
        </radialGradient>
      </defs>
      <rect width="440" height="440" fill="url(#heroGlow)"/>
    </svg>
    <div class="closing-rule"></div>
    <p class="claim">Durch Entgiften und Entschlacken das Wohlbefinden steigern, die Darmgesundheit wieder herstellen, das Gewicht reduzieren und die Heilung für Körper und Geist einleiten.</p>
  </section>
</div>
</body>
</html>
```